81M business card

I need a business card for a life sciences consulting firm I started. The company name is 81M and the logo is attached. I am looking for something edgey and current but different from the blah standard business card.

Industry/Entity Type

Business

Requirements
Nice to have
• Both sides

```html
<!DOCTYPE html>
<html lang="en">
<head>
<meta charset="utf-8">
<title>81M LLC – Business Card</title>
<link rel="stylesheet" href="https://fonts.googleapis.com/css2?family=Open+Sans:wght@400;600;700&family=Roboto+Condensed:wght@400;700&display=swap">
<style>
  :root{
    --bg:#e9e6e1;
    --white:#ffffff;
    --paper:#f4f5f6;
    --navy:#0b2f7a;
    --navy-deep:#071f57;
    --blue:#1a4aa3;
    --orange:#f47a12;
    --ink:#3a3d42;
    --muted:#6b7078;
    --rule:#9aa0a6;
  }
  *{margin:0;padding:0;box-sizing:border-box}
  html,body{width:1200px;height:1024px;overflow:hidden}
  body{background:var(--bg);font-family:"Open Sans",sans-serif;position:relative}

  .card{position:absolute;left:220px;width:760px;height:420px;overflow:hidden;
        box-shadow:0 10px 28px rgba(0,0,0,.22)}

  /* front */
  .card-front{top:52px;background:linear-gradient(180deg,var(--white),var(--paper))}
  .front-band{position:absolute;left:0;right:0;bottom:0;height:38px;background:var(--blue)}
  .front-band-accent{position:absolute;right:0;bottom:0;width:100px;height:38px;background:var(--orange)}
  .brand{position:absolute;left:48px;top:58px;display:flex;align-items:center;gap:14px}
  .brand-dot{width:46px;height:46px;border-radius:50%;background:var(--blue)}
  .brand-name{font-family:"Open Sans",sans-serif;font-weight:700;font-size:52px;line-height:1;color:var(--blue);letter-spacing:1px}
  .brand-tagline{position:absolute;left:110px;top:118px;font-size:12px;color:var(--muted)}
  .divider{position:absolute;left:48px;right:150px;top:200px;height:1px;background:var(--rule)}
  .person-name{position:absolute;right:150px;top:160px;font-family:"Roboto Condensed",sans-serif;font-weight:700;font-size:30px;color:var(--ink);line-height:32px;text-align:right}
  .person-title{position:absolute;right:150px;top:210px;font-family:"Roboto Condensed",sans-serif;font-weight:700;font-size:17px;line-height:20px;color:var(--blue);text-align:right}
  .contacts{position:absolute;left:48px;top:232px;list-style:none}
  .contacts li{display:flex;align-items:center;gap:14px;font-size:17px;color:var(--ink);height:30px}
  .contacts svg{width:16px;height:16px;fill:var(--muted);flex:none}

  /* back */
  .card-back{top:544px;background:radial-gradient(ellipse at 40% 40%,var(--blue) 0%,var(--navy) 55%,var(--navy-deep) 100%)}
  .back-band{position:absolute;left:0;right:0;bottom:0;height:38px;background:var(--orange)}
  .back-brand{position:absolute;left:0;right:0;top:120px;display:flex;flex-direction:column;align-items:center}
  .back-mark{display:flex;align-items:center;gap:18px}
  .back-dot{width:70px;height:70px;border-radius:50%;background:var(--white)}
  .back-name{font-family:"Open Sans",sans-serif;font-weight:700;font-size:96px;line-height:1;color:var(--white);letter-spacing:2px}
  .back-tagline{margin-top:16px;font-size:17px;color:var(--white)}
</style>
</head>
<body>

<section class="card card-front" aria-label="Card front">
  <div class="brand">
    <span class="brand-dot"></span>
    <span class="brand-name">81M LLC</span>
  </div>
  <p class="brand-tagline">regulatory consulting and contract services</p>

  <p class="person-name">Maren Holt</p>
  <div class="divider"></div>
  <p class="person-title">Managing Director</p>

  <ul class="contacts">
    <li><svg viewBox="0 0 16 16"><rect x="4" y="1" width="8" height="14" rx="1.5"/><rect x="5.5" y="3" width="5" height="8" fill="#fff"/></svg>094 512 7783</li>
    <li><svg viewBox="0 0 16 16"><rect x="1" y="3" width="14" height="10" rx="1"/><path d="M1.5 3.5 8 9l6.5-5.5" stroke="#fff" stroke-width="1.4" fill="none"/></svg>maren.holt@81mllc.com</li>
    <li><svg viewBox="0 0 16 16"><circle cx="8" cy="8" r="7"/><path d="M1 8h14M8 1c-3 3-3 11 0 14M8 1c3 3 3 11 0 14" stroke="#fff" stroke-width="1" fill="none"/></svg>www.81mllc.com</li>
    <li><svg viewBox="0 0 16 16"><path d="M8 1a5 5 0 0 0-5 5c0 4 5 9 5 9s5-5 5-9a5 5 0 0 0-5-5z"/><circle cx="8" cy="6" r="2" fill="#fff"/></svg>PO Box 4120 Harlow Park, NSW 2387</li>
  </ul>

  <div class="front-band"></div>
  <div class="front-band-accent"></div>
</section>

<section class="card card-back" aria-label="Card back">
  <div class="back-brand">
    <div class="back-mark">
      <span class="back-dot"></span>
      <span class="back-name">81M LLC</span>
    </div>
    <p class="back-tagline">regulatory consulting and contract services</p>
  </div>
  <div class="back-band"></div>
</section>

</body>
</html>
```